300 x 250 Web Ad for Porn Website

300 x 250 web ad that will appear on a porn site. Need to see 3 options, one with each of the 3 girls. Remove the background around the girls.

Underneath the girls image should read in big bold letters: High Speed Internet
Underneath in slightly smaller size: NO Credit Check

To the left of the girl: Save MONEY...

To the right of the girl: So you can buy more PORN

We want it to look very unique, raunchy, and eye catching.

Target Market(s)

Porn website

Industry/Entity Type

Internet Service Provider

Colors

Designer to choose colors to be used in the design.

Requirements
Must have
• Must stand out so people will definitely notice it.
• JPEG and PNG formats

```html
<!DOCTYPE html>
<html lang="en">
<head>
<meta charset="utf-8">
<title>High Speed Internet – Web Ad Options</title>
<link href="https://fonts.googleapis.com/css2?family=Oswald:wght@400;600;700&family=Roboto:wght@700;900&display=swap" rel="stylesheet">
<style>
  :root {
    --canvas: #121212;
    --purple: #6a1178;
    --purple-deep: #4a0c55;
    --gold-top: #ffd23a;
    --gold-mid: #f5b83a;
    --navy: #1d2a38;
    --navy-deep: #121c27;
    --yellow: #fff200;
    --cyan: #12a9e0;
    --cyan-light: #3ec3ef;
    --pink: #f2074c;
    --white: #ffffff;
    --ink: #1a1a1a;
  }
  * { box-sizing: border-box; margin: 0; padding: 0; }
  html, body { width: 1200px; height: 404px; overflow: hidden; }
  body { background: var(--canvas); position: relative; font-family: "Roboto", Arial, sans-serif; }

  .ad { position: absolute; top: 77px; width: 302px; height: 252px; overflow: hidden; border: 1px solid rgba(255,255,255,0.35); }
  .ad--purple { left: 86px; background: linear-gradient(180deg, var(--gold-top), var(--gold-mid)); }
  .ad--yellow { left: 451px; background: linear-gradient(180deg, var(--navy), var(--navy-deep)); }
  .ad--pink   { left: 815px; background: linear-gradient(180deg, var(--cyan-light), var(--cyan)); }

  .offer-band { position: absolute; left: 0; right: 0; top: 168px; bottom: 0; }
  .ad--purple .offer-band { background: var(--purple); }
  .ad--yellow .offer-band { background: var(--yellow); }
  .ad--pink   .offer-band { background: var(--pink); }

  .model-photo { position: absolute; left: 14px; top: 0; width: 142px; height: 100%; }
  .ad--purple .model-photo { background: linear-gradient(180deg, #3a2418 0%, #b07a5a 40%, #d8c4bc 100%); }
  .ad--yellow .model-photo { background: linear-gradient(180deg, #4a3022 0%, #b9835e 45%, #2a2a2a 100%); }
  .ad--pink   .model-photo { left: 0; width: 160px; background: linear-gradient(180deg, #3a2420 0%, #d69a7c 45%, #c8102e 75%, #d8b89a 100%); }

  .headline { position: absolute; left: 158px; width: 130px; top: 18px; text-align: center; font-family: "Oswald", "Arial Narrow", sans-serif; }
  .save-tag { display: inline-block; padding: 3px 6px; font-weight: 600; font-size: 17px; line-height: 26px; letter-spacing: -0.3px; }
  .pitch { font-weight: 400; font-size: 26px; line-height: 25px; margin-top: 5px; letter-spacing: -0.5px; }
  .punch { font-weight: 700; font-size: 50px; line-height: 50px; letter-spacing: -1px; }

  .ad--purple .save-tag { background: var(--purple); color: var(--white); }
  .ad--purple .pitch { color: var(--purple-deep); }
  .ad--purple .punch { color: var(--purple); }
  .ad--yellow .save-tag { background: var(--yellow); color: var(--ink); }
  .ad--yellow .pitch { color: var(--white); }
  .ad--yellow .punch { color: var(--yellow); }
  .ad--pink .save-tag { background: var(--pink); color: var(--white); }
  .ad--pink .pitch { color: var(--white); }
  .ad--pink .punch { color: var(--yellow); }

  .offer { position: absolute; left: 152px; width: 146px; top: 162px; text-align: center; }
  .privacy-tag { display: inline-block; background: var(--ink); color: var(--white); font-family: "Oswald", sans-serif; font-weight: 600; font-size: 12px; line-height: 15px; padding: 0 6px; border-radius: 8px; }
  .speed { font-weight: 900; font-size: 19px; line-height: 17px; margin-top: 5px; letter-spacing: -0.2px; }
  .credit { font-weight: 700; font-size: 12px; margin-top: 8px; }

  .ad--purple .speed { color: var(--yellow); }
  .ad--purple .credit { color: var(--white); }
  .ad--yellow .speed, .ad--yellow .credit { color: var(--navy-deep); }
  .ad--pink .speed { color: var(--yellow); }
  .ad--pink .credit { color: var(--white); }
</style>
</head>
<body>
  <div class="ad ad--purple">
    <div class="offer-band"></div>
    <div class="model-photo" role="img" aria-label="Cut-out photo of a model in lace lingerie"></div>
    <div class="headline">
      <span class="save-tag">SAVE MONEY</span>
      <p class="pitch">SO YOU CAN<br>BUY MORE</p>
      <p class="punch">PORN!</p>
    </div>
    <div class="offer">
      <span class="privacy-tag">100% PRIVATE</span>
      <p class="speed">HIGH SPEED<br>INTERNET</p>
      <p class="credit">No Credit Check</p>
    </div>
  </div>

  <div class="ad ad--yellow">
    <div class="offer-band"></div>
    <div class="model-photo" role="img" aria-label="Cut-out photo of a model in a black bikini, seen from behind"></div>
    <div class="headline">
      <span class="save-tag">SAVE MONEY</span>
      <p class="pitch">SO YOU CAN<br>BUY MORE</p>
      <p class="punch">PORN!</p>
    </div>
    <div class="offer">
      <span class="privacy-tag">100% PRIVATE</span>
      <p class="speed">HIGH SPEED<br>INTERNET</p>
      <p class="credit">No Credit Check</p>
    </div>
  </div>

  <div class="ad ad--pink">
    <div class="offer-band"></div>
    <div class="model-photo" role="img" aria-label="Cut-out photo of a model in red lingerie with devil horns"></div>
    <div class="headline">
      <span class="save-tag">SAVE MONEY</span>
      <p class="pitch">SO YOU CAN<br>BUY MORE</p>
      <p class="punch">PORN!</p>
    </div>
    <div class="offer">
      <span class="privacy-tag">100% PRIVATE</span>
      <p class="speed">HIGH SPEED<br>INTERNET</p>
      <p class="credit">No Credit Check</p>
    </div>
  </div>
</body>
</html>
```